Online video and marketing company business cards

Need to get some new business cards designed to fit with our new logo. The cards should be professional, clean and simple.

Cards should have:

Name
Position
2 line address
telephone
mobile
email address
web address

We need to have our logo and if possible say what we do...
ONLINE FILM PRODUCTION & STRATEGY

Marketing

```html
<!DOCTYPE html>
<html lang="en">
<head>
<meta charset="utf-8">
<title>Vividreel business card</title>
<link href="https://fonts.googleapis.com/css2?family=Barlow:wght@400;500;600&display=swap" rel="stylesheet">
<style>
  :root {
    --navy: #1c4c7e;
    --sky: #6aa7c4;
    --paper: #ffffff;
    --backdrop: #e6e7e9;
  }
  * { margin: 0; padding: 0; box-sizing: border-box; }
  html, body {
    width: 1096px; height: 1200px; overflow: hidden;
    background: var(--backdrop);
    font-family: "Barlow", Arial, sans-serif;
  }
  .card {
    position: absolute; left: 68px; top: 320px;
    width: 960px; height: 560px;
    background: var(--paper);
    overflow: hidden;
  }
  .band { position: absolute; height: 26px; }
  .band--top-navy { top: 0; left: 0; width: 390px; background: var(--navy); }
  .band--top-sky { top: 0; left: 400px; right: 0; background: var(--sky); }
  .band--bottom-sky { bottom: 0; left: 0; width: 330px; background: var(--sky); }
  .band--bottom-navy { bottom: 0; left: 340px; right: 0; background: var(--navy); }

  .brand {
    position: absolute; left: 150px; top: 92px;
    font-size: 96px; font-weight: 600; line-height: 1;
    color: var(--navy); letter-spacing: -1px;
  }

  .icon-tab {
    position: absolute; left: 0; top: 230px;
    width: 56px; height: 200px;
    background: var(--sky);
    border-radius: 0 12px 12px 0;
  }
  .icon-tab svg { position: absolute; left: 16px; width: 24px; height: 24px; }

  .contact {
    position: absolute; left: 78px; top: 238px;
    list-style: none; color: var(--navy);
    font-size: 21px; font-weight: 500; line-height: 1.2;
  }
  .contact li { height: 38px; display: flex; align-items: center; gap: 10px; white-space: nowrap; }
  .contact .mobile-icon { width: 14px; height: 22px; }

  .name-box {
    position: absolute; left: 620px; top: 318px;
    width: 290px; height: 58px;
    background: var(--sky);
    border-radius: 12px 0 0 12px;
    color: var(--paper);
    font-size: 38px; font-weight: 500; line-height: 58px;
    text-align: right; padding-right: 22px; white-space: nowrap;
  }
  .position {
    position: absolute; left: 620px; top: 386px; width: 290px;
    text-align: right; padding-right: 22px;
    color: var(--navy); font-size: 26px; font-weight: 500;
  }
</style>
</head>
<body>
  <div class="card">
    <div class="band band--top-navy"></div>
    <div class="band band--top-sky"></div>
    <div class="band band--bottom-sky"></div>
    <div class="band band--bottom-navy"></div>

    <div class="brand">vividreel</div>

    <div class="icon-tab">
      <svg style="top:15px" viewBox="0 0 24 24" fill="none" stroke="#fff" stroke-width="2">
        <path d="M12 22s7-7 7-12a7 7 0 0 0-14 0c0 5 7 12 7 12z"/><circle cx="12" cy="10" r="2.5" fill="#fff"/>
      </svg>
      <svg style="top:91px" viewBox="0 0 24 24" fill="none" stroke="#fff" stroke-width="2" stroke-linecap="round">
        <path d="M5 4l4 1 1 4-2 2a12 12 0 0 0 5 5l2-2 4 1 1 4-3 1C10 20 4 14 4 7z"/>
      </svg>
      <svg style="top:129px" viewBox="0 0 24 24" fill="none" stroke="#fff" stroke-width="2">
        <rect x="3" y="6" width="18" height="13"/><path d="M3 6l9 7 9-7M3 19l7-6M21 19l-7-6"/>
      </svg>
      <svg style="top:167px" viewBox="0 0 24 24" fill="none" stroke="#fff" stroke-width="1.8">
        <circle cx="12" cy="12" r="9"/><path d="M3 12h18M12 3v18M5 7h14M5 17h14"/><ellipse cx="12" cy="12" rx="4" ry="9"/>
      </svg>
    </div>

    <ul class="contact">
      <li>Your residentiol or commercial or office address</li>
      <li>in two line</li>
      <li>(00) 00 00000
        <svg class="mobile-icon" viewBox="0 0 14 22"><rect x="1" y="1" width="12" height="20" rx="2" fill="var(--navy)"/><rect x="3" y="4" width="8" height="12" fill="#fff"/></svg>
        (00) 0000000000</li>
      <li>info.support@yourwebsite.com</li>
      <li>www.yourwebsite.com</li>
    </ul>

    <div class="name-box">YOUR NAME</div>
    <div class="position">Position</div>
  </div>
</body>
</html>
```